Love pets? Create a veterinary business card that aligns with our new revamped website.

Greetings! We are a five-doctor veterinary hospital that seeks your expertise in designing a new business card that harmonizes with our recently revitalized website: www.tqrn.net. The card should feature our logo, the five doctors, operating hours, contact information, and communicate our purpose and personality.

Contact Information for Business Card

TBA

```html
<!DOCTYPE html>
<html lang="en">
<head>
<meta charset="utf-8">
<title>Maple Hollow Veterinary Hospital – Business Card</title>
<link rel="stylesheet" href="https://fonts.googleapis.com/css2?family=Montserrat:wght@500;600&family=Didact+Gothic&family=Bangers&display=swap">
<style>
  :root {
    --page-bg: #9a9a9a;
    --card-bg: #ffffff;
    --green: #3faa35;
    --brown: #6e4e12;
    --teal: #6aa5a8;
    --orange: #d4820f;
    --ink: #333333;
    --rule: #555555;
  }
  * { margin: 0; padding: 0; box-sizing: border-box; }
  html, body { width: 1200px; height: 1059px; overflow: hidden; }
  body { background: var(--page-bg); position: relative; font-family: "Montserrat", sans-serif; }

  .card {
    position: absolute;
    left: 255px;
    width: 690px;
    height: 392px;
    background: var(--card-bg);
    border-radius: 22px;
    overflow: hidden;
  }
  .card--front { top: 89px; }
  .card--back { top: 569px; font-family: "Didact Gothic", sans-serif; color: var(--ink); }

  /* Front */
  .front-wave { position: absolute; left: 0; top: 0; width: 690px; height: 392px; }
  .brand { position: absolute; left: 41px; top: 46px; display: flex; align-items: center; gap: 10px; }
  .brand__dot { width: 26px; height: 26px; border-radius: 50%; background: var(--green); }
  .brand__name { font-weight: 600; font-size: 19px; color: var(--green); letter-spacing: 0.2px; }
  .doctors { position: absolute; left: 41px; top: 113px; list-style: none; }
  .doctors li { font-weight: 600; font-size: 21px; line-height: 26.5px; color: var(--brown); letter-spacing: 0.4px; }
  .contacts { position: absolute; left: 41px; top: 232px; list-style: none; }
  .contacts li { display: flex; align-items: center; gap: 8px; font-weight: 500; font-size: 18.5px; line-height: 26.5px; color: var(--ink); letter-spacing: 0.4px; }
  .contacts svg { width: 13px; height: 13px; flex: none; }
  .pet-photos {
    position: absolute; left: 330px; top: 310px; width: 350px; height: 82px;
    border-radius: 40px 40px 0 0;
    background: linear-gradient(90deg, #6a5a4a 0%, #c9a07a 45%, #d8c8b8 100%);
  }

  /* Back */
  .request-title {
    position: absolute; left: 0; right: 0; top: 48px; text-align: center;
    font-family: "Bangers", sans-serif; font-size: 30px; letter-spacing: 0.5px; font-style: italic;
  }
  .request-title .word-green { color: var(--green); }
  .request-title .word-brown { color: var(--brown); }
  .request-note { position: absolute; left: 0; right: 0; top: 79px; text-align: center; font-size: 15.5px; letter-spacing: 0.3px; }
  .field-label { position: absolute; font-size: 17px; }
  .field-line { position: absolute; border-bottom: 1px dashed var(--rule); height: 0; }
  .days { position: absolute; top: 265px; left: 0; width: 100%; }
  .day { position: absolute; display: flex; align-items: center; gap: 10px; font-size: 17px; }
  .day__box { width: 14px; height: 14px; border: 1px solid var(--green); }
  .hours-note { position: absolute; left: 0; right: 0; top: 335px; text-align: center; font-size: 15.5px; letter-spacing: 0.3px; }
  .color-bar { position: absolute; left: 0; bottom: 0; width: 100%; height: 12px; display: flex; }
  .color-bar span { flex: 1; }
  .color-bar .seg-brown { background: var(--brown); }
  .color-bar .seg-green { background: var(--green); }
  .color-bar .seg-teal { background: var(--teal); }
  .color-bar .seg-orange { background: var(--orange); }
</style>
</head>
<body>

<section class="card card--front" aria-label="Business card front">
  <svg class="front-wave" viewBox="0 0 690 392" aria-hidden="true">
    <path d="M0 293 C 70 340, 150 370, 260 365 C 420 358, 560 325, 690 330 L 690 392 L 0 392 Z" fill="var(--brown)"/>
    <path d="M0 305 C 70 350, 150 378, 260 375 C 420 370, 560 342, 690 345 L 690 392 L 0 392 Z" fill="var(--green)"/>
  </svg>

  <div class="brand">
    <span class="brand__dot"></span>
    <span class="brand__name">Maple Hollow Veterinary Hospital</span>
  </div>

  <ul class="doctors">
    <li>Owen Harlow, DVM</li>
    <li>Nina Brandt, DVM</li>
    <li>Clara Wynn, DVM</li>
    <li>Rachel Osei, DVM</li>
  </ul>

  <ul class="contacts">
    <li>
      <svg viewBox="0 0 16 16"><path d="M4 1.5l2.5 3-1.5 1.8a9 9 0 0 0 4.7 4.7l1.8-1.5 3 2.5-1.6 2.5C7.5 14 2 8.5 1.5 3.1z" fill="var(--green)"/></svg>
      (555) 214-7780
    </li>
    <li>
      <svg viewBox="0 0 16 16"><rect x="1" y="3" width="14" height="10" fill="var(--green)"/><path d="M1 3l7 6 7-6" stroke="#fff" stroke-width="1.4" fill="none"/></svg>
      info@tqrn.net
    </li>
    <li>
      <svg viewBox="0 0 16 16"><circle cx="8" cy="8" r="7" fill="var(--green)"/><path d="M1 8h14M8 1c-3 4-3 10 0 14M8 1c3 4 3 10 0 14" stroke="#fff" stroke-width="1" fill="none"/></svg>
      www.tqrn.net
    </li>
  </ul>

  <div class="pet-photos" role="img" aria-label="Photographs of a rottweiler and two cats peeking over the hill"></div>
</section>

<section class="card card--back" aria-label="Business card back">
  <h1 class="request-title"><span class="word-green">REQUEST</span> <span class="word-brown">APPOINTMENT</span></h1>
  <p class="request-note">If this is an emergency, please call the office directly.</p>

  <span class="field-label" style="left:54px; top:144px;">Name</span>
  <span class="field-line" style="left:115px; width:527px; top:162px;"></span>

  <span class="field-label" style="left:54px; top:210px;">Date</span>
  <span class="field-line" style="left:106px; width:196px; top:228px;"></span>
  <span class="field-label" style="left:318px; top:210px;">Time</span>
  <span class="field-line" style="left:371px; width:195px; top:228px;"></span>
  <span class="field-label" style="left:575px; top:210px;">am/pm</span>

  <div class="days">
    <label class="day" style="left:60px;"><span class="day__box"></span>Fri</label>
    <label class="day" style="left:162px;"><span class="day__box"></span>Sat</label>
    <label class="day" style="left:263px;"><span class="day__box"></span>Mon</label>
    <label class="day" style="left:372px;"><span class="day__box"></span>Tue</label>
    <label class="day" style="left:473px;"><span class="day__box"></span>Wed</label>
    <label class="day" style="left:583px;"><span class="day__box"></span>Thu</label>
  </div>

  <p class="hours-note">Now open on Saturdays from 8:00 am-12:00 pm and accepting new clients!</p>

  <div class="color-bar">
    <span class="seg-brown"></span><span class="seg-green"></span><span class="seg-teal"></span><span class="seg-orange"></span>
  </div>
</section>

</body>
</html>
```